Brontello Pizza Website

We are working with Brontello Pizza and designing them a website.

Some sites to use for content/competitors and inspiration:

https://marvettis.example
https://www.tqz.example
https://brightolives.example/en-us/

Thank you for taking the time to consider designing a website for us. We are web developers based in Stockton, CA, USA. Most of our projects go through the same process. Understanding this process may help you win a project with us. We custom-code all of our websites in-house. We don’t have any requirements as to what tools you use for your design, but we prefer Figma files. For any design that we label as four-stars, we send it to the client for review. The client picks the final design they want us to use. Once we complete this process, we will continue to show additional clients all the four-star sites and purchase them later. Your designs will have multiple chances to sell. For better chances of success, we ask that you follow these guidelines.

IMAGES:
If you use any images or icons in the design, we ask that you have a link to the asset so we can purchase the image/icon. Most of the designs we submit do not have the customer’s images on them unless they have some great images. Be creative; show us the feeling you are trying to portray with your image choices. Use any royalty-free site you choose. We subscribe to Corvane and mainly use their images, but we can purchase images outside of Corvane.

PLEASE NOTE: we will not submit designs to clients with watermarks on the images.

FONTS:
We ask that you identify the fonts used in the design. This can be done in a message if you want. We typically use Plinster Fonts and Corvane Fonts.

CONTENT:
We're always open to different content and ideas. We often submit designs with stock images so the client can see our vision. We typically take pictures after the website launch to use their images with our vision. Lorem Ipsum is fine for paragraphs, but we ask that you write the headers in correct English. We want to be able to show the vision and identify the sections of the website.

INSPIRATION:
We typically add a couple of links in the brief of websites we like to help you get started in your design.

REVISIONS:
We do not often ask for revisions of the designs unless we see something in the design that may not appeal to the client. If there are slight changes that we want to make, we do that in the development process.

FEEDBACK:
We rarely give feedback on designs during the design process. We are working on many website projects and do not have the time to provide feedback. We usually respond if your request is well thought out and asks specific questions, but a note asking “feedback, please” usually goes unanswered.

```html
<!DOCTYPE html>
<html lang="en">
<head>
<meta charset="utf-8">
<title>Brontello Pizza</title>
<link href="https://fonts.googleapis.com/css2?family=Bebas+Neue&family=Montserrat:wght@300;400;600;700;800&family=Kaushan+Script&display=swap" rel="stylesheet">
<style>
:root{
  --red:#e62b2b;
  --green:#34a93a;
  --ink:#2b2b2b;
  --white:#ffffff;
  --muted:#444;
}
*{margin:0;padding:0;box-sizing:border-box}
html,body{width:1200px;height:4596px;overflow:hidden;background:var(--white)}
body{position:relative;font-family:'Montserrat',sans-serif;color:var(--ink)}
.abs{position:absolute}
.display{font-family:'Bebas Neue',sans-serif;font-weight:400;line-height:.9}
.script{font-family:'Kaushan Script',cursive}

.nav-link{top:20px;font-family:'Bebas Neue',sans-serif;font-size:13px;letter-spacing:.5px;color:var(--ink)}
.nav-util{top:20px;font-family:'Bebas Neue',sans-serif;font-size:13px;display:flex;align-items:center;gap:6px}
.brand-name{left:500px;top:14px;width:200px;text-align:center;color:var(--ink);font-family:'Bebas Neue',sans-serif;font-size:30px;letter-spacing:1px;line-height:1}

.mega{left:32px;width:1136px;text-align:center;color:var(--ink);font-size:172px;letter-spacing:2px}

.card{border-radius:20px;overflow:hidden}
.photo{position:absolute}
.btn-white{background:var(--white);color:var(--red);font-weight:700;font-size:12px;display:flex;align-items:center;justify-content:center;border-radius:3px;letter-spacing:.3px}
.hero-copy{color:var(--white);font-size:12px;line-height:1.4}

.green-box{background:var(--green);color:var(--white);display:flex;flex-direction:column;align-items:center;justify-content:center}
.green-box .label{font-family:'Bebas Neue',sans-serif;font-size:12px;letter-spacing:.3px}
.green-box .phone{font-family:'Kaushan Script',cursive;font-size:24px;line-height:1}

.social{width:22px;height:22px;border-radius:50%;background:var(--white)}

.product{position:relative;width:262px;height:292px;border:2px solid var(--green);border-radius:4px;text-align:center}
.product .pie{position:absolute;left:46px;top:30px;width:170px;height:72px;border-radius:50%;background:radial-gradient(ellipse at 50% 40%,#f2b24a 0%,#d9622b 55%,#6b4a3a 80%,#333 100%)}
.product h3{position:absolute;top:122px;width:100%;color:var(--red);font-family:'Kaushan Script',cursive;font-weight:400;font-size:26px}
.product p{position:absolute;top:166px;left:30px;right:30px;font-size:10px;line-height:1.25;color:var(--muted)}
.product .price{position:absolute;top:196px;width:100%;font-family:'Kaushan Script',cursive;color:var(--green);font-size:22px}
.product .cart{position:absolute;top:246px;width:100%;font-size:9px;font-weight:700;color:#2d3ea8;text-decoration:underline}

.footer-col h4{font-family:'Bebas Neue',sans-serif;font-weight:400;font-size:17px;margin-bottom:6px}
.footer-col li{list-style:none;font-size:11px;line-height:16px;color:var(--muted)}
.fsocial{width:22px;height:22px;border-radius:50%;background:var(--green)}
</style>
</head>
<body>

<header>
  <span class="abs nav-link" style="left:187px">Order</span>
  <span class="abs nav-link" style="left:241px">Menu</span>
  <span class="abs nav-link" style="left:291px">Catering</span>
  <span class="abs nav-link" style="left:358px">Franchise</span>
  <span class="abs brand-name">Brontello</span>
  <div class="abs nav-util" style="left:796px">
    <svg width="9" height="12" viewBox="0 0 9 12"><path d="M4.5 0a4.5 4.5 0 0 1 4.5 4.5C9 8 4.5 12 4.5 12S0 8 0 4.5A4.5 4.5 0 0 1 4.5 0z" fill="#e62b2b"/><circle cx="4.5" cy="4.5" r="1.6" fill="#fff"/></svg>
    <span>Find Brontello</span>
  </div>
  <div class="abs nav-util" style="left:890px">
    <svg width="10" height="11" viewBox="0 0 10 11"><circle cx="5" cy="3" r="2.6" fill="#e62b2b"/><path d="M0 11c0-3 2.2-5 5-5s5 2 5 5z" fill="#e62b2b"/></svg>
    <span>Login / Signup</span>
  </div>
  <svg class="abs" style="left:995px;top:16px" width="18" height="18" viewBox="0 0 18 18"><circle cx="9" cy="9" r="8" fill="none" stroke="#e62b2b" stroke-width="1.5"/><path d="M5 6h1.2l1.2 5h4.6l1-3.5H7" fill="none" stroke="#e62b2b" stroke-width="1.2"/></svg>
</header>

<h1 class="abs mega display" style="top:122px">Discover the Taste</h1>

<section class="abs card" style="left:30px;top:300px;width:1138px;height:500px">
  <div class="photo" role="img" aria-label="Pizza oven with flames in a dark kitchen" style="inset:0;background:linear-gradient(90deg,#1b140f 0%,#3b2616 45%,#8a4a1a 75%,#d98a2c 100%)"></div>
  <h2 class="abs display" style="left:45px;top:52px;color:#fff;font-size:40px;line-height:.9">Pizza with<br>Italian flair</h2>
  <p class="abs hero-copy" style="left:45px;top:137px;width:215px">Lorem Ipsum is simply dummy text of the printing and typesetting industry. Lorem Ipsum has been the industry's standard dummy text ever since the 1500s,</p>
  <span class="abs script" style="left:910px;top:45px;color:#fff;font-size:42px;transform:rotate(18deg)">Crispy !</span>
  <span class="abs script" style="left:60px;top:370px;color:#fff;font-size:40px;transform:rotate(28deg)">Tasty !</span>
  <div class="abs btn-white" style="left:954px;top:427px;width:132px;height:33px">ORDER NOW</div>
</section>
<div class="abs" role="img" aria-label="Top view of a whole pepperoni and tomato pizza" style="left:359px;top:209px;width:480px;height:480px;border-radius:50%;background:radial-gradient(circle,#e0863a 0%,#c85a24 55%,#a8431d 80%,#d7a55e 92%,#b88244 100%);box-shadow:0 10px 30px rgba(0,0,0,.4)"></div>
<span class="abs script" style="left:560px;top:650px;color:#111;font-size:48px;transform:rotate(-22deg)">Cheesy !</span>

<section class="abs card" style="left:30px;top:833px;width:1138px;height:544px;background:var(--red)">
  <div class="photo" role="img" aria-label="Supreme pizza with peppers, olives and mushrooms on a dark board" style="left:0;top:0;width:505px;height:544px;background:linear-gradient(100deg,#2a2a2a 0%,#b5622e 40%,#d9833d 60%,#e5562e 100%)"></div>
  <div class="abs" style="left:318px;top:85px;width:180px;height:134px;background:var(--green);transform:rotate(-4deg)"></div>
  <span class="abs script" style="left:350px;top:95px;color:var(--red);font-size:48px">50%</span>
  <span class="abs display" style="left:376px;top:155px;color:var(--red);font-size:36px">OFF!</span>
  <span class="abs script" style="left:800px;top:42px;color:#fff;font-size:44px">delicious</span>
  <h2 class="abs display" style="right:157px;top:102px;color:#fff;font-size:140px">Pizza</h2>
  <p class="abs" style="left:651px;top:243px;width:360px;text-align:right;color:#fff;font-size:11.5px;line-height:1.45">Lorem Ipsum is simply dummy text of the printing and typesetting industry. Lorem Ipsum has been the industry's standard dummy text ever since the 1500s, when an unknown printer took a galley of type and scrambled it to make a type specimen book. It has survived not only five centuries.</p>
  <div class="abs green-box" style="left:763px;top:370px;width:205px;height:63px;transform:rotate(-3deg)">
    <span class="label">Delivery Order</span><span class="phone">015-550-2741</span>
  </div>
  <span class="abs" style="left:766px;top:473px;color:#fff;font-size:11px;font-weight:700">Order Now :</span>
  <span class="abs social" style="left:859px;top:470px"></span>
  <span class="abs social" style="left:892px;top:470px"></span>
  <span class="abs social" style="left:925px;top:470px"></span>
  <span class="abs social" style="left:959px;top:470px"></span>
</section>

<section class="abs card" style="left:30px;top:1409px;width:1138px;height:501px">
  <div class="photo" role="img" aria-label="Pepperoni pizza slices with stretching cheese on a dark blurred background" style="inset:0;background:radial-gradient(ellipse at 45% 50%,#5a3526 0%,#2e1c15 55%,#1a110c 100%)"></div>
  <span class="abs script" style="left:255px;top:40px;color:#fff;font-size:70px">brontello</span>
  <h2 class="abs display" style="left:252px;top:138px;color:#fff;font-size:135px">Special</h2>
  <span class="abs" style="left:442px;top:258px;color:#fff;font-size:60px;font-weight:300;line-height:1">PIZZA</span>
  <p class="abs hero-copy" style="left:446px;top:345px;width:340px;font-size:11.5px">Lorem Ipsum is simply dummy text of the printing and typesetting industry. Lorem Ipsum has been the industry's standard dummy text ever since the 1500s,</p>
  <div class="abs btn-white" style="left:446px;top:416px;width:132px;height:33px">ORDER NOW</div>
  <div class="abs green-box" style="left:910px;top:213px;width:228px;height:75px;border-radius:10px 0 0 10px">
    <span class="label">Delivery Order</span><span class="phone" style="font-size:28px">015-550-2741</span>
  </div>
</section>

<h2 class="abs mega display" style="top:1914px;font-size:176px">Italian Fresh Pizza</h2>
<svg class="abs" style="left:34px;top:2068px" width="1134" height="63" viewBox="0 0 1134 63"><polygon points="0,0 1134,0 1112,31.5 1134,63 0,63 22,31.5" fill="#34a93a"/></svg>
<div class="abs" style="left:34px;top:2068px;width:1134px;height:63px;display:flex;align-items:center;justify-content:center;color:#fff;font-weight:700;font-size:22px;letter-spacing:.5px">JOIN THE BRONTELLO WAITLIST NOW!</div>

<span class="abs script" style="left:0;width:1200px;text-align:center;top:2180px;color:var(--red);font-size:42px;line-height:1.2">products</span>
<h2 class="abs display" style="left:0;width:1200px;text-align:center;top:2256px;font-size:56px">Crazy taste with delicious stuff</h2>
<p class="abs" style="left:210px;width:780px;text-align:center;top:2318px;font-size:13px;line-height:1.5">Lorem Ipsum is simply dummy text of the printing and typesetting industry. Lorem Ipsum has been the industry's standard dummy text ever since the 1500s,</p>

<div class="abs" style="left:187px;top:2391px;width:826px;display:grid;grid-template-columns:repeat(3,262px);gap:20px 20px">
  <article class="product"><div class="pie" role="img" aria-label="Italian pizza"></div><h3>italian pizza</h3><p>Lorem Ipsum is simply dummy text of the printing.</p><div class="price">$59.00</div><div class="cart">ADD TO CART</div></article>
  <article class="product"><div class="pie" role="img" aria-label="Italian pizza"></div><h3>italian pizza</h3><p>Lorem Ipsum is simply dummy text of the printing.</p><div class="price">$59.00</div><div class="cart">ADD TO CART</div></article>
  <article class="product"><div class="pie" role="img" aria-label="Italian pizza"></div><h3>italian pizza</h3><p>Lorem Ipsum is simply dummy text of the printing.</p><div class="price">$59.00</div><div class="cart">ADD TO CART</div></article>
  <article class="product"><div class="pie" role="img" aria-label="Italian pizza"></div><h3>italian pizza</h3><p>Lorem Ipsum is simply dummy text of the printing.</p><div class="price">$59.00</div><div class="cart">ADD TO CART</div></article>
  <article class="product"><div class="pie" role="img" aria-label="Italian pizza"></div><h3>italian pizza</h3><p>Lorem Ipsum is simply dummy text of the printing.</p><div class="price">$59.00</div><div class="cart">ADD TO CART</div></article>
  <article class="product"><div class="pie" role="img" aria-label="Italian pizza"></div><h3>italian pizza</h3><p>Lorem Ipsum is simply dummy text of the printing.</p><div class="price">$59.00</div><div class="cart">ADD TO CART</div></article>
  <article class="product"><div class="pie" role="img" aria-label="Italian pizza"></div><h3>italian pizza</h3><p>Lorem Ipsum is simply dummy text of the printing.</p><div class="price">$59.00</div><div class="cart">ADD TO CART</div></article>
  <article class="product"><div class="pie" role="img" aria-label="Italian pizza"></div><h3>italian pizza</h3><p>Lorem Ipsum is simply dummy text of the printing.</p><div class="price">$59.00</div><div class="cart">ADD TO CART</div></article>
  <article class="product"><div class="pie" role="img" aria-label="Italian pizza"></div><h3>italian pizza</h3><p>Lorem Ipsum is simply dummy text of the printing.</p><div class="price">$59.00</div><div class="cart">ADD TO CART</div></article>
</div>

<div class="abs" style="left:528px;top:3352px;width:142px;height:33px;background:var(--red);color:#fff;font-size:12px;font-weight:700;display:flex;align-items:center;justify-content:center;border-radius:3px">VIEW ALL</div>

<section class="abs" style="left:0;top:3461px;width:1200px;height:300px;display:flex">
  <div role="img" aria-label="Delivery person carrying a stack of pizza boxes on a yellow background" style="width:300px;height:300px;background:linear-gradient(135deg,#f6c43a,#e8a82a)"></div>
  <div style="width:300px;height:300px;background:var(--green);color:#fff;display:flex;flex-direction:column;align-items:center;justify-content:center">
    <span class="script" style="font-size:40px;line-height:1.1">follow us</span>
    <span class="display" style="font-size:52px">On Snapfeed</span>
  </div>
  <div role="img" aria-label="Man eating a pizza slice in a restaurant" style="width:300px;height:300px;background:linear-gradient(135deg,#6a5240,#b89a80 60%,#e9e3dc)"></div>
  <div role="img" aria-label="Smiling woman eating pizza at a table" style="width:300px;height:300px;background:linear-gradient(135deg,#3e4a38,#8a7a62 55%,#c9a27a)"></div>
</section>

<section class="abs card" style="left:18px;top:3780px;width:1162px;height:545px;border-radius:16px">
  <div class="photo" role="img" aria-label="Two friends lying down sharing pizza slices" style="inset:0;background:linear-gradient(160deg,#6f7f86 0%,#a07b86 45%,#d7a47a 70%,#c9b6c2 100%)"></div>
  <h2 class="abs display" style="left:0;width:1162px;text-align:center;top:395px;color:#fff;font-size:170px">Stuffed Crazy Crust</h2>
</section>

<footer>
  <div class="abs footer-col" style="left:187px;top:4378px"><h4>Menus</h4><ul><li>Catering</li><li>Restaurants</li><li>Nutritionals</li></ul></div>
  <div class="abs footer-col" style="left:353px;top:4378px"><h4>Locations</h4><ul><li>All Locations</li><li>Search</li></ul></div>
  <div class="abs footer-col" style="left:523px;top:4378px"><h4>About</h4><ul><li>Our Story</li><li>Events</li><li>Blog</li><li>Press</li><li>Talk To Us</li></ul></div>
  <div class="abs footer-col" style="left:679px;top:4378px"><h4>Order</h4><ul><li>Gift Cards</li><li>Ship A Frozen Pizza</li><li>Delivery &amp; Pickup</li></ul></div>
  <div class="abs footer-col" style="left:888px;top:4378px"><h4>Follow us on:</h4>
    <div style="display:flex;gap:11px"><span class="fsocial"></span><span class="fsocial"></span><span class="fsocial"></span><span class="fsocial"></span></div>
  </div>
  <div class="abs" style="left:18px;top:4540px;width:1162px;height:36px;background:var(--ink);color:#fff;font-size:11px;display:flex;align-items:center;justify-content:center">Copyright@2025-All Rights Reserved</div>
</footer>

</body>
</html>
```